Create Vertical Dog Food Labels (3 inches x 5 inches) for Pawlyn Kitchen

We need a packing Vertical label (3 inches x 5 inches) design for our line of Dog Food - Pawlyn Kitchen at pawlynkitchen.com (please review website). This design is for Custom Roll Labels. We have a logo already. Use our logo colors on label. What we need incorporated is a list of our ingredients:

50% Choice Beef
20% Pasture-raised Chicken
15% Brown Rice
15% Fresh Vegetables - Carrots, Kale, Zucchini
Herbal Health Boosters

We also need these lines at the bottom of the label:

Keeps in fridge for 4 days after thawing
Stores in freezer up to 6 months
Questions? email us at orders@brindlecopsepantry.com

We have attached a sample of a competitor. The Meadow Bowl.

Target Market(s)

Dog owners

Industry/Entity Type

Dog Food

Font styles to use
Sans Serif

Requirements
Must have
• Read project description above
Nice to have
• Our logo color incorporated
Should not have
• I want it simple.

```html
<!DOCTYPE html>
<html lang="en">
<head>
<meta charset="utf-8">
<title>Pawlyn Kitchen – Premium Recipe Label</title>
<link href="https://fonts.googleapis.com/css2?family=Outfit:wght@300;400;500;600;700&display=swap" rel="stylesheet">
<style>
  :root {
    --backdrop: #5c5c5c;
    --cream: #fef3d8;
    --orange: #ff5c2d;
    --ink: #2c2a28;
    --green: #0f6b0a;
    --rule: #c9bfa8;
    --divider: #f5a623;
  }
  * { margin: 0; padding: 0; box-sizing: border-box; }
  html, body { width: 1200px; height: 1200px; overflow: hidden; }
  body {
    background: var(--backdrop);
    font-family: "Outfit", sans-serif;
    color: var(--ink);
    position: relative;
  }
  .label {
    position: absolute;
    left: 333px; top: 155px;
    width: 533px; height: 889px;
    background: var(--cream);
    box-shadow: 0 10px 40px rgba(0,0,0,0.25);
    overflow: hidden;
  }
  .label__band { position: absolute; left: 0; top: 0; width: 533px; height: 270px; }
  .label__illustration {
    position: absolute; left: 182px; top: 28px; width: 168px; height: 185px;
    border-radius: 50% 50% 44% 44%;
    background: radial-gradient(circle at 50% 55%, #3a3532 0%, #2c2a28 55%, rgba(44,42,40,0.0) 72%);
  }
  .brand {
    position: absolute; left: 0; top: 290px; width: 533px;
    display: flex; align-items: center; justify-content: center; gap: 14px;
  }
  .brand__dot { width: 60px; height: 60px; border-radius: 50%; background: #7fbb3f; }
  .brand__name { font-size: 32px; font-weight: 500; color: var(--green); letter-spacing: -0.3px; }
  .title { position: absolute; left: 0; width: 533px; text-align: center; }
  .title--kicker { top: 410px; font-size: 25px; font-weight: 300; letter-spacing: 0.5px; }
  .title--main { top: 443px; font-size: 32px; font-weight: 700; color: var(--orange); letter-spacing: -0.3px; }
  .rule { position: absolute; left: 63px; width: 406px; border-top: 1px dashed var(--rule); }
  .tag {
    position: absolute; left: 72px; top: 540px; width: 137px; height: 28px;
    background: var(--ink); color: #fff; font-size: 15px; font-weight: 600;
    display: flex; align-items: center; justify-content: center; letter-spacing: 0.3px;
  }
  .boosters { position: absolute; left: 232px; top: 544px; font-size: 14.5px; font-weight: 600; }
  .ingredient { position: absolute; display: flex; align-items: center; transform: translateY(-50%); }
  .ingredient__pct { font-size: 37px; font-weight: 400; color: var(--orange); line-height: 1; letter-spacing: -1px; }
  .ingredient__name { font-size: 14.5px; font-weight: 600; line-height: 17px; position: absolute; white-space: nowrap; }
  .split { position: absolute; left: 217px; width: 0; height: 34px; border-left: 1px dashed var(--divider); }
  .storage { position: absolute; left: 0; width: 533px; text-align: center; font-size: 17px; font-weight: 400; }
  .storage__rule { position: absolute; left: 125px; top: 754px; width: 283px; border-top: 1px solid var(--rule); }
  .contact__ask { position: absolute; top: 813px; left: 0; width: 533px; text-align: center; font-size: 21px; font-weight: 700; color: var(--orange); }
  .contact__line { position: absolute; top: 841px; left: 0; width: 533px; text-align: center; font-size: 16.5px; font-weight: 300; }
  .contact__line strong { font-weight: 500; }
</style>
</head>
<body>
  <main class="label">
    <svg class="label__band" viewBox="0 0 533 270" aria-hidden="true">
      <path d="M0 0 H533 V252 C480 262 430 240 388 236 C330 232 300 260 270 258 C230 258 190 232 145 236 C90 240 40 262 0 255 Z" fill="#ff5c2d"/>
    </svg>
    <div class="label__illustration" role="img" aria-label="Illustration of a drop falling toward a dog's mouth"></div>

    <div class="brand">
      <span class="brand__dot"></span>
      <span class="brand__name">Pawlyn Kitchen</span>
    </div>

    <p class="title title--kicker">PREMIUM</p>
    <h1 class="title title--main">PAWLYN KITCHEN RECIPE</h1>

    <div class="rule" style="top:538px"></div>
    <div class="tag">INGREDIENTS</div>
    <p class="boosters">Herbal Health Boosters</p>
    <div class="rule" style="top:570px"></div>

    <div class="ingredient" style="left:78px; top:599px"><span class="ingredient__pct">50%</span></div>
    <p class="ingredient__name" style="left:153px; top:582px">Choice<br>Beef</p>
    <div class="split" style="top:582px"></div>
    <div class="ingredient" style="left:232px; top:599px"><span class="ingredient__pct">20%</span></div>
    <p class="ingredient__name" style="left:320px; top:582px">Pasture-raised<br>Chicken</p>

    <div class="rule" style="top:629px"></div>

    <div class="ingredient" style="left:88px; top:658px"><span class="ingredient__pct">15%</span></div>
    <p class="ingredient__name" style="left:153px; top:641px">Brown<br>Rice</p>
    <div class="split" style="top:641px"></div>
    <div class="ingredient" style="left:242px; top:658px"><span class="ingredient__pct">15%</span></div>
    <p class="ingredient__name" style="left:320px; top:640px">Fresh Vegetables -<br>Carrots, Kale, Zucchini</p>

    <div class="rule" style="top:688px"></div>

    <p class="storage" style="top:725px">Keeps in fridge for 4 days after thawing</p>
    <div class="storage__rule"></div>
    <p class="storage" style="top:759px">Stores in freezer up to 6 months</p>

    <p class="contact__ask">Questions?</p>
    <p class="contact__line">email us at: <strong>orders@brindlecopsepantry.com</strong></p>
  </main>
</body>
</html>
```